Etikett für einen Rosé Wein
Zielgruppe
Wir sind ein Weingut und benötigen ein neues Etikett für unseren Muskattrollinger Rosé. Unsere Kunden sind eher traditionelle Weinkäufer.
Aufgabenstellung
Format:
Höhe: 9 cm
Breite: 11 cm
Da es nur ein Vorderetikett gibt, müssen alle relevanten Angaben (Hersteller, Alkohol, Inhalt in L, Rebsorte, etc.) enthalten sein. (siehe Flaschenabbildung anbei)
WÜRTTEMBERG
2019er
Muskattrollinger Rosé
DEUTSCHER QUALITÄTSWEIN
11,0 % Vol.
0,75 l
Enthält Sulfite
A.P.Nr. 58271346
Abfüller
Straße / PLZ / Ort / Tel.
Der Flaschenverschluss ist schwarz d.h. das neue Etikettendesign sollte dazu passen.
Bisher ist der Hintergrund des Weinetiketts schwarz. Dies muss jedoch nicht so bleiben.
Im Anhang finden Sie außerdem ein Plakat. Ggf. können Sie für das Flaschendesign einige nostalgische Elemente davon übernehmen.

```html
<!DOCTYPE html>
<html lang="de">
<head>
<meta charset="utf-8">
<title>Muskattrollinger Rosé – Etikett</title>
<link rel="stylesheet" href="https://fonts.googleapis.com/css2?family=Bebas+Neue&family=Playfair+Display:wght@400;700&display=swap">
<style>
  :root {
    --peach: #fdcfaa;
    --coral: #ec6a50;
    --coral-text: #e5533d;
    --white: #ffffff;
    --cream: #fdf6ef;
  }
  html, body {
    margin: 0;
    padding: 0;
    overflow: hidden;
    background: var(--peach);
  }
  .label {
    position: relative;
    width: 1200px;
    height: 982px;
    background: var(--peach);
    overflow: hidden;
  }
  .rose-art {
    position: absolute;
    left: 0;
    top: 0;
    width: 440px;
    height: 982px;
    background:
      radial-gradient(ellipse 230px 250px at 230px 270px, var(--coral) 0%, var(--coral) 55%, rgba(236,106,80,0) 100%),
      radial-gradient(ellipse 110px 70px at 230px 560px, var(--coral) 0%, rgba(236,106,80,0) 100%),
      linear-gradient(90deg, rgba(236,106,80,0.55) 0%, rgba(236,106,80,0.35) 40%, rgba(236,106,80,0) 100%);
  }
  .leaf-art {
    position: absolute;
    right: 0;
    top: 545px;
    width: 250px;
    height: 437px;
    background: radial-gradient(ellipse 120px 200px at 140px 240px, var(--cream) 0%, rgba(253,246,239,0.6) 55%, rgba(253,246,239,0) 100%);
  }
  .variety {
    position: absolute;
    left: 111px;
    top: 192px;
    margin: 0;
    font-family: "Bebas Neue", "Arial Narrow", sans-serif;
    font-weight: 400;
    font-size: 142px;
    line-height: 142px;
    letter-spacing: 2px;
    color: var(--white);
  }
  .quality {
    position: absolute;
    right: 117px;
    top: 340px;
    margin: 0;
    text-align: right;
    font-family: "Playfair Display", Georgia, serif;
    font-weight: 700;
    font-size: 55px;
    line-height: 67px;
    color: var(--coral-text);
  }
  .bottler {
    position: absolute;
    left: 115px;
    top: 692px;
    margin: 0;
    font-family: "Playfair Display", Georgia, serif;
    font-weight: 400;
    font-size: 31px;
    line-height: 35px;
    color: var(--white);
    font-style: normal;
  }
  .legal {
    position: absolute;
    left: 109px;
    top: 850px;
    margin: 0;
    font-family: "Playfair Display", Georgia, serif;
    font-weight: 400;
    font-size: 31px;
    line-height: 35px;
    color: var(--white);
  }
  .volume {
    position: absolute;
    right: 117px;
    top: 796px;
    margin: 0;
    text-align: right;
    font-family: "Playfair Display", Georgia, serif;
    font-weight: 700;
    font-size: 55px;
    line-height: 69px;
    color: var(--coral-text);
  }
</style>
</head>
<body>
  <main class="label">
    <div class="rose-art" role="img" aria-label="Illustration einer Rose mit Stiel und Blättern in Korallrot"></div>
    <div class="leaf-art" role="img" aria-label="Helle Blätterzweig-Illustration am rechten Rand"></div>

    <h1 class="variety">Muskattrollinger<br>Rosé</h1>

    <p class="quality">Deutscher Qualitätswein<br>Württemberg 2019</p>

    <address class="bottler">
      Abfüller:<br>
      Musterstraße 12<br>
      Musterstadt 54367<br>
      07431 287905
    </address>

    <p class="legal">A.P.Nr. 58271346<br>Enthält Sulfite</p>

    <p class="volume">750ml<br>11,0% Vol.</p>
  </main>
</body>
</html>
```